Sleek and Morden Business Card

Business Card Design for Business Name "Lantern Pine Services (LPS)"
Offering Virtual Assistant (VA) services including Virtual Receptionist, Appointment and Diary Management. Taking and Answering calls for Sole Trader Businesses. Quotes, Invoices, Expense Reconciliation, Accounts Payable and Accounts Receivable.
Lantern Services offers clients the ease of a complete office without the physical need to having an office.
Target Market(s)
Target market are Sole Traders like Electricians, Plumbers, Painters etc.
Industry/Entity Type
Business
Colors
Designer to choose colors to be used in the design.
Look and feel
Each slider illustrates characteristics of the customer's brand and the style your logo design should communicate.

```html
<!DOCTYPE html>
<html lang="en">
<head>
<meta charset="utf-8">
<title>Lantern Pine Services – Business Card</title>
<link rel="stylesheet" href="https://fonts.googleapis.com/css2?family=Jost:wght@300;400&display=swap">
<style>
  :root {
    --page: #ffffff;
    --ink: #000000;
    --brand-brown: #a57c52;
    --card-white: #ffffff;
    --photo-warm: #e9a866;
    --photo-cream: #fbeedb;
    --photo-pale: #f7e3c6;
    --photo-dark: #3a2614;
  }
  * { margin: 0; padding: 0; box-sizing: border-box; }
  html, body { width: 1200px; height: 900px; overflow: hidden; background: var(--page); }
  body { position: relative; font-family: "Jost", "Futura", sans-serif; color: var(--ink); }

  .side-label {
    position: absolute; top: 46px; width: 390px; text-align: center;
    font-size: 46px; font-weight: 400; line-height: 1;
  }
  .side-label--front { left: 141px; }
  .side-label--back { left: 663px; }

  .card { position: absolute; top: 129px; width: 391px; height: 702px; overflow: hidden; }
  .card--front { left: 141px; }
  .card--back { left: 663px; background: var(--brand-brown); }

  .card__photo {
    position: absolute; left: 0; top: 0; width: 100%; height: 639px;
    background:
      linear-gradient(160deg, transparent 0 38%, rgba(58,38,20,0.85) 38% 48%, transparent 48%),
      linear-gradient(180deg, var(--photo-warm) 0%, var(--photo-cream) 35%, var(--photo-pale) 70%, var(--photo-dark) 88%, var(--photo-dark) 100%);
  }

  .contact { position: absolute; right: 27px; top: 385px; text-align: right; }
  .contact__name { font-size: 29px; line-height: 1.1; }
  .contact__role { font-size: 22px; line-height: 1.3; }
  .contact__phone { font-size: 24px; line-height: 1.35; margin-top: 2px; }
  .contact__email { font-size: 15px; line-height: 1.4; }
  .contact__label { margin-right: 18px; }
  .contact__phone .contact__label { margin-right: 10px; }

  .tagline-band {
    position: absolute; left: 0; bottom: 0; width: 100%; height: 63px;
    background: var(--brand-brown); color: var(--card-white);
    display: flex; align-items: center; justify-content: center;
    font-size: 22px;
  }

  .brand { position: absolute; left: 0; top: 294px; width: 100%; text-align: center; color: var(--card-white); }
  .brand__name { font-size: 22px; line-height: 1; }
  .brand__initials {
    font-size: 70px; font-weight: 300; letter-spacing: 14px; line-height: 1;
    margin-top: 14px; padding-left: 14px;
  }
</style>
</head>
<body>
  <div class="side-label side-label--front">front</div>
  <div class="side-label side-label--back">back</div>

  <section class="card card--front">
    <div class="card__photo" role="img" aria-label="Soft-focus photo of hands typing on a keyboard in warm light"></div>
    <div class="contact">
      <p class="contact__name">Mara Kellings</p>
      <p class="contact__role">Owner</p>
      <p class="contact__phone"><span class="contact__label">Mobile :</span>0400 555 218</p>
      <p class="contact__email"><span class="contact__label">Email :</span>mara@lanternpine.com.au</p>
    </div>
    <div class="tagline-band">"Lantern Pine Services (LPS)"</div>
  </section>

  <section class="card card--back">
    <div class="brand">
      <p class="brand__name">Lantern Pine Services</p>
      <p class="brand__initials">(LPS)</p>
    </div>
  </section>
</body>
</html>
```